Business Card Design Project

colors are orange and blue (marlow crest university football orange and blue.

need jpeg to build a business card
fill 2/3 of biz card on top half of card

I need a orange swoosh (looks like a line painted by a paintbrush used on outside of the house) the orange line should trail off at the end.
underscore the orange swoosh with a blue shelf.make the left side of the shelf ornamental like it fits into the corner of the wall

Target Market(s)

life coach business consultant. orange means enthusiasm and blue is stability and competence

Industry/Entity Type

University

Requirements
Must have
• add very simple paint example. orange must be marlow crest u football color orange and same w/ the blue. orange is to be like a wide paint brush. blue below will look like a shelf w/ an edge that fits into a corner wall.

```html
<!DOCTYPE html>
<html lang="en">
<head>
<meta charset="utf-8">
<title>Marlow Crest University – Business Card</title>
<link href="https://fonts.googleapis.com/css2?family=Anton&display=swap" rel="stylesheet">
<style>
  :root {
    --card-bg: #ffffff;
    --card-edge: #9a9a9a;
    --crest-orange: #fd4f1a;
    --crest-blue: #0a3cff;
  }
  html, body {
    margin: 0;
    padding: 0;
    width: 1200px;
    height: 695px;
    overflow: hidden;
    background: var(--card-bg);
  }
  .business-card {
    position: relative;
    width: 1200px;
    height: 695px;
    box-sizing: border-box;
    border: 2px solid var(--card-edge);
    background: var(--card-bg);
    overflow: hidden;
  }
  .brand-name {
    position: absolute;
    left: 52px;
    top: 40px;
    display: flex;
    align-items: center;
    gap: 14px;
    margin: 0;
    font-family: "Anton", sans-serif;
    font-weight: 400;
    font-size: 56px;
    line-height: 0.95;
    letter-spacing: 1px;
    text-transform: uppercase;
    color: var(--crest-blue);
  }
  .brand-mark {
    width: 26px;
    height: 26px;
    background: var(--crest-blue);
    flex: none;
  }
  .paint-swoosh {
    position: absolute;
    left: 0;
    top: 0;
    width: 1200px;
    height: 695px;
  }
  .swoosh-orange { fill: var(--crest-orange); }
  .shelf-blue { fill: var(--crest-blue); }
</style>
</head>
<body>
  <div class="business-card">
    <h1 class="brand-name">
      <span class="brand-mark" aria-hidden="true"></span>
      <span>Marlow<br>Crest</span>
    </h1>
    <svg class="paint-swoosh" viewBox="0 0 1200 695" aria-hidden="true">
      <path class="swoosh-orange"
        d="M3,349 C250,250 550,185 765,182 C900,180 1100,200 1197,248
           L1197,281 C1080,235 900,220 765,223 C520,228 250,270 3,349 Z"/>
      <path class="shelf-blue"
        d="M109,341 C300,285 550,242 765,239 C950,237 1130,260 1197,295
           L1197,315 C1130,285 950,246 765,248 C550,250 320,290 109,341 Z"/>
    </svg>
  </div>
</body>
</html>
```